Business card - PK Talent Partners / The Darwell Group

We need a business card and logo design for my executive search (recruiting / headhunting) firm. We find people to fill open jobs at companies. We are a U.S. based company and do some global work also. So maybe something with a globe but definitely looking for other options also. Maybe something incorporating the letters PK which is our current logo but looking at options. The card should say BOTH full company names and tag line-

PK Talent Partners / The Darwell Group
Leadership Placement Results You Can Trust

The design should say about the company-
Sharp
Reliable
Find the best people for the job
Business oriented
Results achieved
Modern

Target Market(s)

Business owners, CEO's, and heads of human resources departments

Industry/Entity Type

Business Consultant

Contact Information for Business Card

The card MUST say BOTH full company names and tag line-

Logo Text

Logo does not NEED to say anything on the design itself, but could if designed that way.

Font styles to use
Serif
Sans Serif

Requirements
Must have
• The business cards need to have. In addition to name, title, address, phone, website, and email address,
• The card MUST say BOTH full company names and tag line-
• PK Talent Partners / The Darwell Group
• Leadership Placement Results You Can Trust
Nice to have
• The design should say about the company-
• Sharp
• Reliable
• Find the best people for the job
• Business oriented
• Results achieved
• Modern
• Maybe something with a globe or the letters PK or relating to people. Open to options.
Should not have
• Should not be cutesy or funny, for this design

```html
<!DOCTYPE html>
<html lang="en">
<head>
<meta charset="utf-8">
<title>PK Talent Partners – Business Card</title>
<link rel="stylesheet" href="https://fonts.googleapis.com/css2?family=Archivo:wght@700&family=Open+Sans:wght@300;400;600;700&display=swap">
<style>
  :root {
    --stage: #ebe8e3;
    --charcoal: #3c3c3e;
    --ink: #2b2b2d;
    --gold: #b8935a;
    --paper: #fbfbfa;
    --rule: #8a8a8c;
    --light: #f1f1f1;
  }
  * { box-sizing: border-box; margin: 0; padding: 0; }
  html, body { width: 1200px; height: 800px; overflow: hidden; }
  body {
    background: var(--stage);
    font-family: "Open Sans", Arial, sans-serif;
    position: relative;
  }

  /* Brand lockup shown above the cards */
  .lockup {
    position: absolute; top: 70px; left: 0; width: 1200px;
    display: flex; flex-direction: column; align-items: center;
  }
  .brand-name {
    display: flex; align-items: center; gap: 12px;
    font-family: "Archivo", Arial, sans-serif; font-weight: 700;
    color: var(--ink); font-size: 30px; letter-spacing: 0.5px;
    white-space: nowrap;
  }
  .brand-dot { width: 16px; height: 16px; border-radius: 50%; background: var(--gold); flex: none; }
  .group-line {
    display: flex; align-items: center; gap: 10px; margin-top: 6px;
    color: var(--gold); font-size: 15px; letter-spacing: 2px; text-transform: uppercase;
    white-space: nowrap;
  }
  .group-line::before, .group-line::after {
    content: ""; width: 70px; height: 1px; background: var(--rule);
  }
  .tagline { color: var(--gold); font-size: 14px; margin-top: 5px; font-weight: 300; white-space: nowrap; }

  /* Cards */
  .card {
    position: absolute; top: 300px; width: 500px; height: 286px;
    border-radius: 3px; overflow: hidden;
    box-shadow: 0 10px 28px rgba(0,0,0,0.22);
  }
  .card-back {
    left: 70px; background: var(--charcoal);
    display: flex; flex-direction: column; align-items: center; justify-content: center;
  }
  .card-back .brand-name { color: var(--light); font-size: 28px; }
  .card-back .group-line::before, .card-back .group-line::after { background: var(--light); }

  .card-front { left: 630px; background: var(--paper); }
  .front-brand {
    height: 160px; display: flex; flex-direction: column;
    align-items: center; justify-content: center;
  }
  .front-brand .brand-name { font-size: 24px; }
  .front-brand .group-line { font-size: 13px; }
  .front-brand .tagline { font-size: 12.5px; }
  .gold-rule { height: 4px; background: var(--gold); }
  .contact-band {
    height: 122px; background: var(--charcoal);
    display: flex; align-items: center; padding: 0 34px;
  }
  .person { width: 170px; text-align: right; padding-right: 24px; }
  .person-name { color: var(--gold); font-weight: 700; font-size: 15px; letter-spacing: 0.5px; text-transform: uppercase; white-space: nowrap; }
  .person-title { color: var(--light); font-size: 11px; margin-top: 3px; }
  .band-divider { width: 1px; height: 70px; background: var(--gold); }
  .contacts { list-style: none; padding-left: 24px; }
  .contacts li {
    display: flex; align-items: center; gap: 9px;
    color: var(--light); font-size: 13.5px; line-height: 1.75; white-space: nowrap;
  }
  .icon { width: 14px; height: 14px; flex: none; }
</style>
</head>
<body>

  <header class="lockup">
    <div class="brand-name"><span class="brand-dot"></span>PK Talent Partners</div>
    <div class="group-line">The Darwell Group</div>
    <div class="tagline">Leadership Placement Results You Can Trust</div>
  </header>

  <section class="card card-back">
    <div class="brand-name"><span class="brand-dot"></span>PK Talent Partners</div>
    <div class="group-line">The Darwell Group</div>
    <div class="tagline">Leadership Placement Results You Can Trust</div>
  </section>

  <section class="card card-front">
    <div class="front-brand">
      <div class="brand-name"><span class="brand-dot"></span>PK Talent Partners</div>
      <div class="group-line">The Darwell Group</div>
      <div class="tagline">Leadership Placement Results You Can Trust</div>
    </div>
    <div class="gold-rule"></div>
    <div class="contact-band">
      <div class="person">
        <div class="person-name">Dana Whitford</div>
        <div class="person-title">Director</div>
      </div>
      <div class="band-divider"></div>
      <ul class="contacts">
        <li>
          <svg class="icon" viewBox="0 0 14 14"><rect width="14" height="14" rx="2" fill="#b8935a"/><path d="M4.2 3.2l1.6 0 .7 2-1 .8c.5 1.1 1.3 1.9 2.4 2.4l.8-1 2 .7v1.6c0 .5-.4.8-.9.8C6.6 10.4 3.6 7.4 3.4 4.1c0-.5.3-.9.8-.9z" fill="#3c3c3e"/></svg>
          902-555-0148
        </li>
        <li>
          <svg class="icon" viewBox="0 0 14 14"><rect width="14" height="14" rx="2" fill="#b8935a"/><rect x="3" y="4.2" width="8" height="5.6" fill="none" stroke="#3c3c3e" stroke-width="1"/><path d="M3 4.2l4 3.2 4-3.2" fill="none" stroke="#3c3c3e" stroke-width="1"/></svg>
          dana@pktalentpartners.ca
        </li>
        <li>
          <svg class="icon" viewBox="0 0 14 14"><rect width="14" height="14" rx="2" fill="#b8935a"/><circle cx="7" cy="7" r="3.8" fill="none" stroke="#3c3c3e" stroke-width="1"/><path d="M3.2 7h7.6M7 3.2c-1.6 2.2-1.6 5.4 0 7.6M7 3.2c1.6 2.2 1.6 5.4 0 7.6" fill="none" stroke="#3c3c3e" stroke-width="0.9"/></svg>
          www.pktalentpartners.ca
        </li>
      </ul>
    </div>
  </section>

</body>
</html>
```